Responsive, beautiful email sign-up process pages

My client wants to re-imagine their email newsletter sign up process. The funnel currently starts in the first panel of their home page carousel at:

https://thriftbeacon.co.uk/

It is also featured in the right side of the footer.

I would like to start, what could become a full template re-design project by optimising this crucial user journey. I am attaching the screenshots from the current user journey below and it would be great to get some designs that improve on the look and feel.

Thank you,
Dorian

Target Market(s)

People who want to maximise the interest rate they receive on their cash savings.

Industry/Entity Type

Financial Service

Coding

Coded - Design and coding required

Number of Pages Required

4 page

Font styles to use
Sans Serif

Requirements
Must have
• A well designed, responsive design for all of the elements of the user journey funnel that works well on desktop, laptop, tablet and phone. The site is currently using Bootstrap 3.* for the responsive templates, so it would be useful to continue leveraging these libraries, but in a much more visually appealing way.
• It is felt that the current overall site is dull and unprofessional, so we are using this as a way of showing how much better it could be, which should lead to a sitewide "facelift".
Nice to have
• Creative use of css, svg and javascript to optimise the user experience on all target platforms.
Should not have
• Non-responsive designs.

```html
<!DOCTYPE html>
<html lang="en">
<head>
<meta charset="utf-8">
<title>Thrift Beacon – Savings Information</title>
<link rel="stylesheet" href="https://fonts.googleapis.com/css2?family=Open+Sans:wght@400;600;700;800&family=Oswald:wght@400;500&display=swap">
<style>
:root{
  --orange:#f26b21;
  --orange-dark:#d9571a;
  --ink:#2b2b2b;
  --text:#555;
  --muted:#8a8a8a;
  --light:#f2f2f2;
  --line:#dcdcdc;
  --dark:#333333;
  --darker:#232323;
  --darkest:#1a1a1a;
  --white:#ffffff;
}
*{box-sizing:border-box;margin:0;padding:0}
html,body{width:700px;height:1200px;overflow:hidden}
body{font-family:"Open Sans",Arial,sans-serif;color:var(--text);background:#e9e9e9;position:relative}
.heading{font-family:"Oswald","Arial Narrow",sans-serif;font-weight:400;letter-spacing:.5px;color:var(--ink)}
.accent{color:var(--orange)}

/* top bar */
.topbar{height:18px;background:var(--darker);display:flex;align-items:center;justify-content:space-between;padding:0 30px;font-size:6.5px;color:#ddd;font-weight:600;letter-spacing:.3px}
.topbar nav{display:flex;gap:14px}
.topbar nav a:first-child{color:var(--orange)}
.topbar .account{display:flex;gap:12px;align-items:center}
.topbar .phone{color:var(--white)}

/* header */
.header{height:64px;background:var(--white);display:flex;align-items:center;justify-content:space-between;padding:0 30px;border-bottom:1px solid var(--line)}
.brand{display:flex;align-items:center;gap:6px;font-weight:700;font-size:15px;color:var(--ink)}
.brand-dot{width:14px;height:14px;border-radius:50%;background:var(--orange)}
.mainnav{display:flex;gap:0;font-size:6.5px;font-weight:700;letter-spacing:.3px}
.mainnav a{padding:8px 7px;color:var(--ink);border-left:1px solid var(--line)}
.mainnav a:first-child{border-left:none}

a{text-decoration:none;color:inherit}

/* hero */
.hero{height:198px;position:relative;background:linear-gradient(90deg,#f7f7f7 0%,#ececec 55%,#d9d4cf 100%);overflow:hidden}
.hero-photo{position:absolute;right:0;top:0;width:380px;height:198px;background:linear-gradient(120deg,#e9e6e2 0%,#d8c4b0 45%,#c7a98e 70%,#e2dcd5 100%)}
.hero-copy{position:absolute;left:40px;top:46px;width:320px}
.hero-title{font-size:15px;font-weight:800;color:var(--ink);letter-spacing:.2px}
.hero-list{list-style:none;margin-top:10px}
.hero-list li{font-size:9.5px;font-weight:700;color:var(--ink);margin-bottom:5px;display:flex;align-items:center;gap:7px}
.hero-list li::before{content:"";width:5px;height:5px;background:var(--orange);border-radius:50%}
.btn{display:inline-block;background:var(--orange);color:var(--white);font-size:7px;font-weight:700;padding:6px 11px;letter-spacing:.4px}
.hero .btn{margin-top:8px}

/* specialist advice */
.advice{margin:6px 30px 0;height:238px;background:var(--white);box-shadow:0 1px 4px rgba(0,0,0,.15);padding:16px 26px 0;text-align:center}
.advice h2{font-size:20px}
.advice .intro{font-size:6.5px;line-height:1.5;color:var(--muted);margin:5px auto 0;width:460px}
.advice-grid{display:flex;gap:16px;margin-top:12px;text-align:left}
.advice-card{flex:1}
.advice-image{height:82px}
.advice-card h3{font-size:11px;font-weight:600;color:var(--orange);margin-top:7px}
.advice-card p{font-size:6.5px;line-height:1.5;color:var(--muted);margin-top:3px}
.more{display:block;width:8px;height:3px;background:var(--orange);margin-top:5px}

/* welcome + news */
.info{display:flex;gap:24px;padding:16px 30px 0;height:178px}
.welcome{flex:1.7;background:var(--white);padding:14px 16px}
.news{flex:1;background:var(--white);padding:14px 14px}
.section-title{display:flex;align-items:center;gap:7px;font-size:15px}
.icon-circle{width:16px;height:16px;border-radius:50%;background:var(--orange);display:flex;align-items:center;justify-content:center}
.welcome p{font-size:6.8px;line-height:1.6;color:var(--muted);margin-top:8px}
.news-item{display:flex;gap:8px;margin-top:9px;align-items:flex-start}
.news-date{width:26px;flex:none;text-align:center;font-weight:700;color:var(--white)}
.news-date .day{display:block;background:var(--dark);font-size:10px;padding:2px 0}
.news-date .month{display:block;background:var(--orange);font-size:5.5px;padding:1px 0}
.news-item h4{font-size:6.8px;font-weight:700;color:var(--ink)}
.news-item p{font-size:6px;color:var(--muted);margin-top:2px;line-height:1.4}

/* review */
.review{margin-top:14px;height:197px;background:var(--dark);text-align:center;padding-top:16px;position:relative}
.review h2{font-size:19px;color:var(--white)}
.review .sub{font-size:6.5px;color:#bbb;margin-top:3px}
.quote{position:absolute;left:60px;top:66px;width:500px;height:70px;background:var(--white);text-align:left;padding:16px 18px 0 32px;font-size:7px;line-height:1.6;color:var(--text)}
.quote-mark{position:absolute;left:12px;top:12px;font-size:20px;color:var(--orange);font-family:Georgia,serif;line-height:1}
.avatar{position:absolute;left:582px;top:62px;width:64px;height:64px;border-radius:50%;border:3px solid var(--white);background:linear-gradient(160deg,#c9b5a2,#6f6a66)}
.reviewer{position:absolute;right:54px;top:142px;font-size:6.5px;color:#ccc}
.dots{position:absolute;left:60px;top:152px;display:flex;gap:5px}
.dots span{width:6px;height:6px;border-radius:50%;background:#888}
.dots span:first-child{background:var(--white)}

/* press strip */
.press{height:70px;background:var(--white);display:flex;align-items:center;justify-content:space-between;padding:0 14px}
.press-items{display:flex;align-items:center;justify-content:space-around;flex:1;color:var(--ink)}
.press-name{font-size:17px;font-weight:700}
.press-badge{width:26px;height:26px;background:#bdbdbd}
.arrow{width:14px;height:20px}

/* footer */
.footer{height:190px;background:var(--darker);display:flex;gap:18px;padding:18px 30px 0;color:#bbb}
.footer-col{flex:1}
.footer-col h5{font-size:7.5px;font-weight:700;color:var(--white);letter-spacing:.3px}
.footer-col ul{list-style:none;margin-top:7px}
.footer-col li{font-size:6.3px;line-height:1.75}
.footer-col li::before{content:"› ";color:var(--orange)}
.footer-col p{font-size:6.3px;line-height:1.6;margin-top:7px}
.social{display:flex;gap:10px;margin-top:12px}
.social span{width:12px;height:12px;border-radius:50%;background:#777}
.signup-input{margin-top:10px;height:16px;background:var(--white);font-size:6px;color:var(--muted);padding:4px 6px}
.footer .btn{margin-top:6px;padding:4px 12px}

.bottombar{height:20px;background:var(--darkest);font-size:6.2px;color:#aaa;display:flex;align-items:center;justify-content:center}
</style>
</head>
<body>

<div class="topbar">
  <nav><a href="#">HOME</a><a href="#">TESTIMONIALS</a><a href="#">ABOUT US</a><a href="#">CONTACT US</a></nav>
  <div class="account"><span>LOGIN</span><span>SIGN UP</span><span class="phone">0800 555 0142</span></div>
</div>

<header class="header">
  <div class="brand"><span class="brand-dot"></span>thriftbeacon.co.uk</div>
  <nav class="mainnav">
    <a href="#">CONCIERGE SERVICE</a><a href="#">BEST BUY TABLES</a><a href="#">RATE TRACKING</a><a href="#">NEWS AND ALERTS</a><a href="#">ADVICE AND GUIDES</a><a href="#">AWARDS</a>
  </nav>
</header>

<section class="hero">
  <div class="hero-photo" role="img" aria-label="Smiling couple reviewing their savings on a laptop"></div>
  <div class="hero-copy">
    <h1 class="hero-title">GET <span class="accent">FREE</span> WHOLE OF MARKET INFORMATION</h1>
    <ul class="hero-list">
      <li>UNCOMPROMISED BEST BUY TABLES</li>
      <li>ACCOUNT MONITORING AND ALERT SERVICES</li>
      <li>ACCESS TO SAVINGS EXPERTS</li>
    </ul>
    <a class="btn" href="#">READ MORE</a>
  </div>
</section>

<section class="advice">
  <h2 class="heading">SPECIALIST <span class="accent">ADVICE</span></h2>
  <p class="intro">Our team reviews hundreds of savings accounts every week so you can compare rates, spot better deals and move your money with confidence.</p>
  <div class="advice-grid">
    <article class="advice-card">
      <div class="advice-image" role="img" aria-label="Coins and calculator on a desk" style="background:linear-gradient(135deg,#d8d2c8,#9b9285)"></div>
      <h3>£100,000 Plus in Savings?</h3>
      <p>Tailored guidance for larger balances, helping you spread cash safely across trusted banks.</p>
      <span class="more"></span>
    </article>
    <article class="advice-card">
      <div class="advice-image" role="img" aria-label="Adviser meeting with a client" style="background:linear-gradient(135deg,#c9b7a4,#6d5e52)"></div>
      <h3>Wealth Management</h3>
      <p>Independent support to plan, protect and grow your wealth over the long term.</p>
      <span class="more"></span>
    </article>
    <article class="advice-card">
      <div class="advice-image" role="img" aria-label="Saver checking rates on a tablet" style="background:linear-gradient(135deg,#e2dad0,#a89884)"></div>
      <h3>Take Our £50 Challenge</h3>
      <p>See how much extra interest you could earn in minutes with our quick check.</p>
      <span class="more"></span>
    </article>
  </div>
</section>

<section class="info">
  <div class="welcome">
    <h2 class="section-title heading"><span class="icon-circle"><svg width="8" height="8" viewBox="0 0 8 8"><circle cx="4" cy="4" r="2" fill="#fff"/></svg></span>WELCOME TO <span class="accent">THRIFT BEACON</span></h2>
    <p>Thrift Beacon has helped savers find better interest rates since 2002. We track the whole market daily and alert you the moment your rate drops or a better deal appears.</p>
    <p>Our concierge service can handle the legwork for larger balances, while our free tools, best buy tables and guides keep every saver informed about where their money works hardest.</p>
  </div>
  <div class="news">
    <h2 class="section-title heading"><span class="icon-circle"><svg width="8" height="8" viewBox="0 0 8 8"><rect x="1" y="1.5" width="6" height="5" fill="none" stroke="#fff" stroke-width="1"/></svg></span>LATEST NEWS</h2>
    <div class="news-item"><div class="news-date"><span class="day">12</span><span class="month">JUN</span></div><div><h4>Fixed rate bonds edge higher this week</h4><p>A quick look at the best new deals.</p></div></div>
    <div class="news-item"><div class="news-date"><span class="day">12</span><span class="month">JUN</span></div><div><h4>Easy access rates slip at major banks</h4><p>Check whether your account is affected today.</p></div></div>
    <div class="news-item"><div class="news-date"><span class="day">14</span><span class="month">JUN</span></div><div><h4>New ISA season: what savers should know</h4><p>Allowances, deadlines and top transfer tips inside.</p></div></div>
  </div>
</section>

<section class="review">
  <h2 class="heading" style="color:#fff">OUR CUSTOMER <span class="accent">REVIEW</span></h2>
  <p class="sub">Read what savers say about our rate tracking and concierge service.</p>
  <blockquote class="quote"><span class="quote-mark">“</span>I had no idea how much interest I was missing. The alerts told me exactly when to move my money, and the best buy tables made switching simple and stress free.</blockquote>
  <div class="avatar" role="img" aria-label="Portrait of reviewer"></div>
  <p class="reviewer">Alana Morrow, Leeds</p>
  <div class="dots"><span></span><span></span><span></span></div>
</section>

<section class="press">
  <svg class="arrow" viewBox="0 0 14 20"><path d="M10 3 L4 10 L10 17" fill="none" stroke="#999" stroke-width="2"/></svg>
  <div class="press-items">
    <span class="press-name">KBN NEWS</span>
    <span class="press-name">Daily Ledger</span>
    <span class="press-name">the herald line</span>
    <span class="press-badge"></span>
    <span class="press-name">NORTHMOOR</span>
  </div>
  <svg class="arrow" viewBox="0 0 14 20"><path d="M4 3 L10 10 L4 17" fill="none" stroke="#999" stroke-width="2"/></svg>
</section>

<footer class="footer">
  <div class="footer-col">
    <h5>QUICK LINKS</h5>
    <ul><li>Home</li><li>Concierge Service</li><li>Best Buy Tables</li><li>Rate Tracker</li><li>News and Alerts</li><li>Advice and Guides</li><li>Awards</li><li>Testimonials</li><li>About Us</li><li>Contact Us</li></ul>
  </div>
  <div class="footer-col">
    <h5>TOP SAVINGS ACCOUNTS</h5>
    <ul><li>High Interest Current Accounts</li><li>Easy Access</li><li>Fixed Rate Bonds</li><li>Variable Rate ISAs</li><li>Fixed Rate ISAs</li><li>Notice Accounts</li><li>Monthly Income</li><li>Regular Savings</li><li>Children's Accounts</li></ul>
  </div>
  <div class="footer-col">
    <h5>WE'RE WORKING FOR A BETTER DEAL FOR SAVERS</h5>
    <p>Thrift Beacon campaigns for fairer rates and clearer terms, so loyal savers are never left behind.</p>
    <div class="social"><span></span><span></span></div>
  </div>
  <div class="footer-col">
    <h5>SIGN UP FOR OUR NEWSLETTER</h5>
    <p>Stay in the loop with the latest rates, alerts and savings tips delivered straight to your inbox.</p>
    <div class="signup-input">Enter Email</div>
    <a class="btn" href="#">SUBMIT</a>
  </div>
</footer>

<div class="bottombar">Copyright © 2015 Thrift Beacon &nbsp;|&nbsp; Terms &amp; Conditions &nbsp;|&nbsp; Privacy Policy</div>

</body>
</html>
```